Ridgely Forge business card for handing simple contact information and generating service awareness

Utilizing the attached logo(s), generate a professional, but approachable, card conveying a sense of capability and integrity. Please only use one logo of the four attached; the different colors are all acceptable, but preference will be given to a design integrating a teal/turquoise logo,

I do not know where to put in the contact information or details?

Target Market(s)

Agriculture, Farming, Timber, Forestry, Construction, Crane Service

Industry/Entity Type

Contact Information for Business Card

Name, Phone Number, email address

Colors

Designer to choose colors to be used in the design.

Requirements
Nice to have
• It would be great to have either a mountain or one of the attached cranes as a backdrop on the rear of the card. Simple watermarks and/or Debossing is also great

```html
<!DOCTYPE html>
<html lang="en">
<head>
<meta charset="utf-8">
<title>Ridgely Forge – Business Card</title>
<link href="https://fonts.googleapis.com/css2?family=Inter:wght@400;700&display=swap" rel="stylesheet">
<style>
  :root {
    --backdrop: #c4c4c4;
    --forest: #2c6e5f;
    --forest-deep: #276556;
    --forest-light: #3a7d6c;
    --paper: #f6f6f6;
    --paper-tone: #e8e8e8;
    --ink: #111111;
    --ink-soft: #555555;
    --white: #ffffff;
  }
  html, body {
    margin: 0;
    width: 1200px;
    height: 1200px;
    overflow: hidden;
    background: var(--backdrop);
    font-family: "Inter", sans-serif;
  }
  .canvas { position: relative; width: 1200px; height: 1200px; }
  .card {
    position: absolute;
    left: 226px;
    width: 746px;
    height: 436px;
    border-radius: 22px;
    overflow: hidden;
  }
  .card-front { top: 118px; background: var(--forest); }
  .card-back { top: 611px; background: var(--paper); }

  /* Tonal repeat of the name across the front */
  .repeat-field { position: absolute; left: 0; top: -10px; width: 100%; }
  .tile-row { display: flex; height: 94px; white-space: nowrap; }
  .tile-row.row-a { margin-left: 16px; }
  .tile-row.row-b { margin-left: -36px; }
  .tile {
    flex: 0 0 121px;
    height: 94px;
    display: flex; flex-direction: column; align-items: center; justify-content: center;
    gap: 6px;
  }
  .tile-dot { width: 38px; height: 38px; border-radius: 50%; background: var(--forest-deep); }
  .tile-name { font-size: 12px; font-weight: 700; color: var(--forest-light); letter-spacing: 0.3px; }
  .tile.is-hidden { visibility: hidden; }

  .brand-mark {
    position: absolute;
    left: 559px; top: 262px;
    width: 141px; height: 94px;
    display: flex; flex-direction: column; align-items: center; justify-content: center;
    gap: 6px;
  }
  .brand-dot { width: 44px; height: 44px; border-radius: 50%; background: var(--white); }
  .brand-name { color: var(--white); font-weight: 700; font-size: 15px; letter-spacing: 0.4px; white-space: nowrap; }

  /* Back */
  .contact {
    position: absolute;
    left: 0; width: 380px;
    top: 156px;
    text-align: center;
  }
  .person-name { margin: 0; font-size: 27px; font-weight: 700; color: var(--ink); }
  .person-role { margin: 6px 0 0; font-size: 16px; letter-spacing: 2px; color: var(--ink-soft); }
  .contact-icons { display: flex; justify-content: center; gap: 6px; margin-top: 20px; }
  .contact-icons svg { width: 30px; height: 30px; }
  .contact-line { margin: 8px 0 0; font-size: 21px; color: var(--ink-soft); line-height: 1.2; }
  .contact-line + .contact-line { margin-top: 4px; }

  .back-brand {
    position: absolute;
    left: 360px; top: 36px;
    width: 420px; height: 360px;
  }
  .back-brand-circle {
    position: absolute; left: 80px; top: 0;
    width: 250px; height: 250px; border-radius: 50%;
    background: var(--paper-tone);
  }
  .back-brand-name {
    position: absolute; left: 4px; top: 262px;
    font-size: 50px; font-weight: 700;
    color: var(--paper-tone);
    white-space: nowrap;
  }
</style>
</head>
<body>
<div class="canvas">
  <section class="card card-front">
    <div class="repeat-field" aria-label="Tonal repeat of the company name">
      <div class="tile-row row-a">
        <div class="tile"><span class="tile-dot"></span><span class="tile-name">Ridgely Forge</span></div>
        <div class="tile"><span class="tile-dot"></span><span class="tile-name">Ridgely Forge</span></div>
        <div class="tile"><span class="tile-dot"></span><span class="tile-name">Ridgely Forge</span></div>
        <div class="tile"><span class="tile-dot"></span><span class="tile-name">Ridgely Forge</span></div>
        <div class="tile"><span class="tile-dot"></span><span class="tile-name">Ridgely Forge</span></div>
        <div class="tile"><span class="tile-dot"></span><span class="tile-name">Ridgely Forge</span></div>
        <div class="tile"><span class="tile-dot"></span><span class="tile-name">Ridgely Forge</span></div>
      </div>
      <div class="tile-row row-b">
        <div class="tile"><span class="tile-dot"></span><span class="tile-name">Ridgely Forge</span></div>
        <div class="tile"><span class="tile-dot"></span><span class="tile-name">Ridgely Forge</span></div>
        <div class="tile"><span class="tile-dot"></span><span class="tile-name">Ridgely Forge</span></div>
        <div class="tile"><span class="tile-dot"></span><span class="tile-name">Ridgely Forge</span></div>
        <div class="tile"><span class="tile-dot"></span><span class="tile-name">Ridgely Forge</span></div>
        <div class="tile"><span class="tile-dot"></span><span class="tile-name">Ridgely Forge</span></div>
        <div class="tile"><span class="tile-dot"></span><span class="tile-name">Ridgely Forge</span></div>
      </div>
      <div class="tile-row row-a">
        <div class="tile"><span class="tile-dot"></span><span class="tile-name">Ridgely Forge</span></div>
        <div class="tile"><span class="tile-dot"></span><span class="tile-name">Ridgely Forge</span></div>
        <div class="tile"><span class="tile-dot"></span><span class="tile-name">Ridgely Forge</span></div>
        <div class="tile"><span class="tile-dot"></span><span class="tile-name">Ridgely Forge</span></div>
        <div class="tile"><span class="tile-dot"></span><span class="tile-name">Ridgely Forge</span></div>
        <div class="tile"><span class="tile-dot"></span><span class="tile-name">Ridgely Forge</span></div>
        <div class="tile"><span class="tile-dot"></span><span class="tile-name">Ridgely Forge</span></div>
      </div>
      <div class="tile-row row-b">
        <div class="tile"><span class="tile-dot"></span><span class="tile-name">Ridgely Forge</span></div>
        <div class="tile"><span class="tile-dot"></span><span class="tile-name">Ridgely Forge</span></div>
        <div class="tile"><span class="tile-dot"></span><span class="tile-name">Ridgely Forge</span></div>
        <div class="tile"><span class="tile-dot"></span><span class="tile-name">Ridgely Forge</span></div>
        <div class="tile"><span class="tile-dot"></span><span class="tile-name">Ridgely Forge</span></div>
        <div class="tile is-hidden"><span class="tile-dot"></span><span class="tile-name">Ridgely Forge</span></div>
        <div class="tile"><span class="tile-dot"></span><span class="tile-name">Ridgely Forge</span></div>
      </div>
      <div class="tile-row row-a">
        <div class="tile"><span class="tile-dot"></span><span class="tile-name">Ridgely Forge</span></div>
        <div class="tile"><span class="tile-dot"></span><span class="tile-name">Ridgely Forge</span></div>
        <div class="tile"><span class="tile-dot"></span><span class="tile-name">Ridgely Forge</span></div>
        <div class="tile"><span class="tile-dot"></span><span class="tile-name">Ridgely Forge</span></div>
        <div class="tile"><span class="tile-dot"></span><span class="tile-name">Ridgely Forge</span></div>
        <div class="tile"><span class="tile-dot"></span><span class="tile-name">Ridgely Forge</span></div>
        <div class="tile"><span class="tile-dot"></span><span class="tile-name">Ridgely Forge</span></div>
      </div>
    </div>
    <div class="brand-mark">
      <span class="brand-dot"></span>
      <span class="brand-name">Ridgely Forge</span>
    </div>
  </section>

  <section class="card card-back">
    <div class="back-brand" aria-label="Large debossed company name">
      <span class="back-brand-circle"></span>
      <span class="back-brand-name">Ridgely Forge</span>
    </div>
    <div class="contact">
      <h1 class="person-name">Name Surname</h1>
      <p class="person-role">POSITION</p>
      <div class="contact-icons">
        <svg viewBox="0 0 30 30" aria-label="Phone">
          <circle cx="15" cy="15" r="15" fill="var(--forest)"/>
          <path d="M10.5 8.5c.6-.6 1.5-.5 2 .1l1.5 2c.4.5.3 1.2-.1 1.6l-.9.9c.8 1.6 2.2 3 3.8 3.8l.9-.9c.4-.4 1.1-.5 1.6-.1l2 1.5c.6.5.7 1.4.1 2l-1 1c-1 1-2.6 1.2-4 .5-3.2-1.6-5.8-4.2-7.4-7.4-.7-1.4-.5-3 .5-4z" fill="var(--white)"/>
        </svg>
        <svg viewBox="0 0 30 30" aria-label="Email">
          <circle cx="15" cy="15" r="15" fill="var(--forest)"/>
          <rect x="8" y="10" width="14" height="10" rx="1.2" fill="var(--white)"/>
          <path d="M8.5 10.8 15 15.6l6.5-4.8" fill="none" stroke="var(--forest)" stroke-width="1.4"/>
        </svg>
      </div>
      <p class="contact-line">555-014-2290</p>
      <p class="contact-line">hello@ridgelyforge.com</p>
    </div>
  </section>
</div>
</body>
</html>
```